Creative Stationary For Security Solutions Company
Halvern Guard Services
Creative Stationary For Security Solutions Company - Security
Creative Brief
Professional
Wesley Kolvasky
wesley@halvernguard.example
www.halvernguard.example
California PI No. 51928 And California PPO No. 40261
Logo has been uploaded in different color variations. Feel free to experiment, however I prefer the logo with black highlights on the visor, nose and neck (#1 I believe) I will provide my phone numbers towards the end of the project. Thanks and have fun.
I would like to see my logo on one side and info on the other. But feel free to experiment.

```html
<!DOCTYPE html>
<html lang="en">
<head>
<meta charset="utf-8">
<title>Halvern Guard Services – Business Card</title>
<link rel="stylesheet" href="https://fonts.googleapis.com/css2?family=Montserrat:wght@400;600;800&display=swap">
<style>
  :root {
    --bg: #e4e4e6;
    --card-black: #1d1d1f;
    --card-black-deep: #121213;
    --paper: #f7f7f7;
    --orange: #f26a1b;
    --ink: #2a2a2a;
    --white: #ffffff;
    --muted: #9a9a9a;
  }
  * { box-sizing: border-box; margin: 0; padding: 0; }
  html, body {
    width: 1200px; height: 864px; overflow: hidden;
    background: var(--bg);
    font-family: "Montserrat", sans-serif;
  }
  .stage {
    width: 1200px; height: 864px;
    display: flex; align-items: center; justify-content: center; gap: 30px;
  }
  .card {
    position: relative;
    width: 560px; height: 320px;
    border-radius: 22px;
    overflow: hidden;
    box-shadow: 0 10px 26px rgba(0,0,0,.18);
  }

  /* Front */
  .card-front {
    background: radial-gradient(ellipse at 50% 40%, #2a2a2c 0%, var(--card-black) 55%, var(--card-black-deep) 100%);
    display: flex; flex-direction: column; align-items: center; justify-content: center;
  }
  .front-brand {
    display: flex; align-items: center; gap: 14px;
    margin-top: 20px;
  }
  .brand-dot {
    width: 34px; height: 34px; border-radius: 50%;
    background: var(--orange);
  }
  .front-brand-name {
    color: var(--white);
    font-weight: 800; font-size: 22px; letter-spacing: .5px;
  }
  .front-web {
    margin-top: 58px;
    font-size: 13px; letter-spacing: 3.5px; font-weight: 600;
    color: var(--white);
  }
  .front-web .accent { color: var(--orange); }

  /* Back */
  .card-back { background: var(--paper); }
  .back-shapes { position: absolute; inset: 0; }
  .back-brand {
    position: absolute; left: 34px; top: 96px;
    display: flex; align-items: center; gap: 12px;
  }
  .back-brand-name {
    color: var(--ink);
    font-weight: 800; font-size: 21px; line-height: 1.15;
    width: 170px;
  }
  .person { position: absolute; left: 36px; top: 206px; }
  .person-name { color: var(--orange); font-weight: 600; font-size: 13px; }
  .person-role { color: var(--ink); font-size: 11px; margin-top: 2px; }
  .contact {
    position: absolute; right: 26px; top: 58px;
    list-style: none;
    color: var(--white); font-size: 11px;
  }
  .contact li { display: flex; align-items: center; gap: 8px; margin-bottom: 7px; }
  .contact svg { width: 13px; height: 13px; flex: none; }
</style>
</head>
<body>
<main class="stage">

  <section class="card card-front" aria-label="Card front">
    <div class="front-brand">
      <span class="brand-dot"></span>
      <span class="front-brand-name">Halvern Guard Services</span>
    </div>
    <p class="front-web">www.<span class="accent">HalvernGuard</span>.example</p>
  </section>

  <section class="card card-back" aria-label="Card back">
    <svg class="back-shapes" viewBox="0 0 560 320" preserveAspectRatio="none" aria-hidden="true">
      <path d="M250 0 H560 V320 H0 V300 C160 300 300 250 340 150 C365 90 330 35 250 0 Z" fill="var(--card-black)"/>
      <path d="M0 292 C160 292 292 244 330 148 C354 90 322 36 240 0" fill="none" stroke="var(--orange)" stroke-width="7"/>
      <path d="M0 278 C150 280 278 236 316 146" fill="none" stroke="var(--card-black)" stroke-width="3"/>
    </svg>

    <div class="back-brand">
      <span class="brand-dot"></span>
      <span class="back-brand-name">Halvern Guard Services</span>
    </div>

    <div class="person">
      <p class="person-name">Wesley Kolvasky</p>
      <p class="person-role">Founder</p>
    </div>

    <ul class="contact">
      <li>
        <svg viewBox="0 0 14 14"><circle cx="7" cy="7" r="7" fill="var(--white)"/><path d="M4.5 3.5l1.4 0 .6 1.8-.9.6a5 5 0 0 0 2.5 2.5l.6-.9 1.8.6v1.4c-3.6.3-6.3-2.4-6-6z" fill="var(--card-black)"/></svg>
        123-456-7890
      </li>
      <li>
        <svg viewBox="0 0 14 14"><circle cx="7" cy="7" r="7" fill="var(--white)"/><path d="M4.5 3.5l1.4 0 .6 1.8-.9.6a5 5 0 0 0 2.5 2.5l.6-.9 1.8.6v1.4c-3.6.3-6.3-2.4-6-6z" fill="var(--card-black)"/></svg>
        987-654-3210
      </li>
      <li>
        <svg viewBox="0 0 14 14"><circle cx="7" cy="7" r="7" fill="var(--white)"/><rect x="4" y="5" width="6" height="4" fill="var(--card-black)"/></svg>
        123-456-7890
      </li>
      <li>
        <svg viewBox="0 0 14 14"><circle cx="7" cy="7" r="7" fill="var(--white)"/><path d="M3.5 4.5h7v5h-7z M3.5 4.5l3.5 2.8 3.5-2.8" fill="none" stroke="var(--card-black)" stroke-width="1"/></svg>
        wesley@halvernguard.example
      </li>
      <li>
        <svg viewBox="0 0 14 14"><circle cx="7" cy="7" r="7" fill="var(--white)"/><circle cx="7" cy="7" r="3.5" fill="none" stroke="var(--card-black)" stroke-width="1"/><path d="M3.5 7h7M7 3.5v7" stroke="var(--card-black)" stroke-width=".8"/></svg>
        www.halvernguard.example
      </li>
    </ul>
  </section>

</main>
</body>
</html>
```